Namecard for wristwatch company

I run a watch company named Varnik which just launched our first watch. I need a namecard design that is unique and something very different. It should be the same size or smaller than the usual cards. It will be printed on the usual paper as metal/wood are nice but might be too expensive.
I have attached some photos of my watch and the company logo as well.

Target Market(s)
Watch collectors, young professionals
Industry/Entity Type
It Company
Look and feel
Each slider illustrates characteristics of the customer's brand and the style your logo design should communicate.

```html
<!DOCTYPE html>
<html lang="en">
<head>
<meta charset="utf-8">
<title>Varnik – Business Card</title>
<link rel="stylesheet" href="https://fonts.googleapis.com/css2?family=Open+Sans:wght@400;600;700&display=swap">
<style>
  :root {
    --backdrop: #2e2f31;
    --card-top: #ffffff;
    --card-bottom: #e4e5e7;
    --brand-blue: #0db0ef;
    --charcoal: #464749;
    --ink: #2b2b2b;
    --white: #ffffff;
  }
  * { margin: 0; padding: 0; box-sizing: border-box; }
  html, body {
    width: 1200px; height: 816px; overflow: hidden;
    background: var(--backdrop);
    font-family: "Open Sans", Arial, sans-serif;
  }
  .stage {
    width: 1200px; height: 816px;
    display: flex; align-items: center; justify-content: center;
  }
  .card {
    position: relative;
    width: 1000px; height: 580px;
    border-radius: 44px;
    overflow: hidden;
    background: radial-gradient(ellipse at 65% 30%, var(--card-top) 0%, var(--card-bottom) 100%);
  }
  .card__shapes { position: absolute; inset: 0; }
  .brand {
    position: absolute; top: 130px; right: 110px;
    display: flex; align-items: center; gap: 18px;
  }
  .brand__dot {
    width: 34px; height: 34px; border-radius: 50%;
    border: 6px solid var(--charcoal);
  }
  .brand__name {
    font-size: 58px; font-weight: 700; color: var(--brand-blue);
    letter-spacing: 3px;
  }
  .identity { position: absolute; left: 56px; top: 206px; }
  .identity__name {
    font-size: 38px; font-weight: 700; color: var(--brand-blue);
    text-transform: uppercase; letter-spacing: 0.5px; line-height: 1.1;
  }
  .identity__role {
    font-size: 27px; font-weight: 400; color: var(--brand-blue);
    margin-top: 2px;
  }
  .contacts {
    position: absolute; left: 56px; top: 330px;
    list-style: none; color: var(--ink);
  }
  .contacts__item {
    display: flex; align-items: flex-start; gap: 12px;
    font-size: 24px; line-height: 32px;
  }
  .contacts__item--address { font-weight: 700; margin-bottom: 2px; }
  .contacts__icon { width: 24px; height: 32px; flex: none; fill: var(--brand-blue); }
  .web {
    position: absolute; left: 560px; right: 0; top: 385px; height: 93px;
    display: flex; align-items: center; justify-content: center;
    padding-left: 20px;
    font-size: 34px; color: var(--white); letter-spacing: 0.5px;
  }
</style>
</head>
<body>
<main class="stage">
  <article class="card">
    <svg class="card__shapes" viewBox="0 0 1000 580" width="1000" height="580" aria-hidden="true">
      <path d="M0,515 L470,515 C510,515 520,468 560,468 L1000,468 L1000,580 L0,580 Z" fill="var(--brand-blue)"/>
      <path d="M606,385 L1000,385 L1000,478 L606,478 A46.5,46.5 0 0 1 606,385 Z" fill="var(--charcoal)"/>
    </svg>

    <div class="brand">
      <span class="brand__dot"></span>
      <span class="brand__name">VARNIK</span>
    </div>

    <header class="identity">
      <h1 class="identity__name">Zelos Varnik</h1>
      <p class="identity__role">Managing Director</p>
    </header>

    <ul class="contacts">
      <li class="contacts__item contacts__item--address">
        <svg class="contacts__icon" viewBox="0 0 24 32"><path d="M12 4a8 8 0 0 0-8 8c0 6 8 16 8 16s8-10 8-16a8 8 0 0 0-8-8zm0 11a3 3 0 1 1 0-6 3 3 0 0 1 0 6z"/></svg>
        <span>27 Kestrel Lane, 4th floor<br>Brookfield BN2</span>
      </li>
      <li class="contacts__item">
        <svg class="contacts__icon" viewBox="0 0 24 32"><path d="M2 14c0-3 4-5 10-5s10 2 10 5v2h-6v-2h-8v2H2zM5 18h14l2 8H3z"/></svg>
        <span>012 480 3157</span>
      </li>
      <li class="contacts__item">
        <svg class="contacts__icon" viewBox="0 0 24 32"><path d="M4 12h16v14H4zM7 8h10v3H7z"/></svg>
        <span>012 480 3158</span>
      </li>
      <li class="contacts__item">
        <svg class="contacts__icon" viewBox="0 0 24 32"><path d="M2 11h20v13H2zm2 2 8 6 8-6z"/></svg>
        <span>zelos@varnikwatch.com</span>
      </li>
    </ul>

    <p class="web">www.varnikwatch.com</p>
  </article>
</main>
</body>
</html>
```